Meridale Family Law Firm Website Renovation

We need a website redesign in SquareSpace that is more modern, user friendly, on brand, less cluttered, easier to navigate, conveys clearly what our services are, and has clear, visible calls to action.

We would like to hire and work with the winning designer to complete the remaining pages of the site.

Target Market(s)

Couples looking for divorce representation or mediation who have a conscious, progressive mindset. They are self-aware and personal development plays an important role in their lives. They want an amicable interaction and aspire to have a healthy relationship after divorce.

Age range: 30-60
Income 100K+ household

Industry/Entity Type

Family Law

Font styles to use
Sans Serif

Colors
85acd3
33a6d7
50c0af
a0cd3a

Requirements
Must have
• Please see attached doc for full creative brief details.

"Changing the way people divorce" on top of site.
Images that show happy clients and that represent males and females. Diversity inclusion is also be important.
We are looking for warm, welcoming design and imagery.
Should not have
• Not heavily attorney focused.
Please see attached brief for full description.

```html
<!DOCTYPE html>
<html lang="en">
<head>
<meta charset="utf-8">
<title>Meridale Family Law &amp; Mediation</title>
<link href="https://fonts.googleapis.com/css2?family=Josefin+Sans:wght@300;400&family=Montserrat:ital,wght@0,400;0,500;0,600;0,700;1,400&display=swap" rel="stylesheet">
<style>
:root{
  --green:#57c1a3;
  --blue:#2f9dd8;
  --blue-soft:#85acd3;
  --lime:#a0cd3a;
  --ink:#2b2b2b;
  --text:#4a4a4a;
  --mute:#7a7a7a;
  --dark:#333436;
  --gray:#eceef1;
  --white:#fff;
}
*{box-sizing:border-box;margin:0;padding:0}
html,body{width:1200px;height:5059px;overflow:hidden;background:var(--white)}
body{position:relative;font-family:"Montserrat",sans-serif;color:var(--text)}
.abs{position:absolute}
h1,h2,h3,h4,h5{font-weight:400}
.heading{font-family:"Josefin Sans",sans-serif;font-weight:300;color:var(--ink)}
.btn{display:inline-block;font-size:11px;padding:7px 14px;color:#fff;background:var(--dark)}

/* header */
.site-header{top:0;left:0;width:1200px;height:79px;border-bottom:1px solid #e3e3e3}
.brand{left:143px;top:8px;display:flex;align-items:center;gap:14px}
.brand-dot{width:62px;height:62px;border-radius:50%;background:var(--green)}
.brand-name{font-size:13px;font-weight:600;letter-spacing:3px;color:var(--ink);text-transform:uppercase}
.nav{left:431px;top:38px;display:flex;gap:20px;font-size:10.5px;color:var(--ink)}
.header-cta{left:927px;top:24px}
.header-cta small{display:block;font-size:9.5px;color:var(--ink)}
.header-cta strong{display:block;font-size:19px;color:var(--blue);font-weight:600;letter-spacing:.8px;margin-top:1px}

/* photo fills */
.photo-hero{left:0;top:80px;width:1200px;height:529px;background:
  radial-gradient(ellipse 170px 130px at 1010px 150px,rgba(214,168,132,.85),transparent 70%),
  radial-gradient(ellipse 150px 120px at 770px 170px,rgba(205,160,128,.8),transparent 70%),
  radial-gradient(ellipse 130px 110px at 590px 190px,rgba(196,156,126,.7),transparent 70%),
  radial-gradient(ellipse 340px 200px at 880px 470px,rgba(28,40,66,.95),transparent 75%),
  radial-gradient(ellipse 500px 300px at 1100px 20px,rgba(226,226,222,.55),transparent 70%),
  linear-gradient(180deg,#6f7276 0%,#3c4048 45%,#1c1f24 80%,#111316 100%)}
.photo-band{left:369px;top:1210px;width:464px;height:259px;background:
  radial-gradient(ellipse 60px 110px at 245px 130px,rgba(60,64,74,.9),transparent 75%),
  radial-gradient(ellipse 50px 70px at 330px 200px,rgba(70,60,58,.85),transparent 75%),
  radial-gradient(ellipse 45px 60px at 160px 210px,rgba(64,58,56,.8),transparent 75%),
  linear-gradient(180deg,#b9c6d2 0%,#d3d6d6 28%,#8f8c82 38%,#b59f7c 55%,#8e7653 100%)}
.photo-svc1{left:609px;top:1650px;width:591px;height:412px;background:
  radial-gradient(ellipse 120px 110px at 150px 60px,rgba(196,150,118,.85),transparent 70%),
  radial-gradient(ellipse 140px 120px at 340px 230px,rgba(180,132,104,.8),transparent 70%),
  radial-gradient(ellipse 110px 110px at 530px 200px,rgba(150,108,86,.8),transparent 70%),
  radial-gradient(ellipse 120px 90px at 180px 280px,rgba(210,212,214,.7),transparent 70%),
  radial-gradient(ellipse 400px 160px at 320px 420px,rgba(24,32,48,.95),transparent 75%),
  linear-gradient(180deg,#a9a8a4 0%,#6d6c6a 40%,#2c3240 100%)}
.photo-svc2{left:0;top:2082px;width:589px;height:416px;background:
  radial-gradient(ellipse 90px 80px at 330px 120px,rgba(222,186,158,.9),transparent 70%),
  radial-gradient(ellipse 120px 180px at 330px 260px,rgba(236,232,228,.85),transparent 70%),
  radial-gradient(ellipse 160px 260px at 90px 300px,rgba(22,30,48,.95),transparent 75%),
  radial-gradient(ellipse 140px 260px at 540px 300px,rgba(28,30,38,.95),transparent 75%),
  linear-gradient(180deg,#d7d4cf 0%,#b7b3ad 50%,#4d5a70 100%)}
.photo-quiz{left:141px;top:3107px;width:466px;height:271px;background:
  radial-gradient(ellipse 80px 70px at 200px 190px,rgba(212,170,140,.85),transparent 70%),
  radial-gradient(ellipse 90px 70px at 350px 190px,rgba(214,182,150,.85),transparent 70%),
  radial-gradient(ellipse 60px 100px at 90px 90px,rgba(150,100,84,.7),transparent 70%),
  radial-gradient(ellipse 70px 110px at 290px 80px,rgba(170,168,172,.7),transparent 70%),
  linear-gradient(180deg,#f0ede8 0%,#e3ddd5 60%,#d8cfc4 100%)}
.portrait{height:244px;background:
  radial-gradient(ellipse 60px 75px at 50% 42%,rgba(200,160,132,.9),transparent 72%),
  radial-gradient(ellipse 110px 70px at 50% 100%,rgba(40,44,52,.95),transparent 75%),
  linear-gradient(180deg,#e9eaec,#c9ccd0)}
.portrait.warm{background:
  radial-gradient(ellipse 80px 95px at 50% 40%,rgba(214,120,70,.75),transparent 72%),
  radial-gradient(ellipse 55px 65px at 50% 44%,rgba(236,196,170,.95),transparent 72%),
  radial-gradient(ellipse 110px 70px at 50% 100%,rgba(30,32,40,.95),transparent 75%),
  linear-gradient(180deg,#eeeeee,#d8d8d8)}

/* hero card */
.hero-card{left:65px;top:193px;width:342px;height:300px;background:#fff;padding:76px 0 0 38px}
.hero-card h1{font-size:30px;line-height:1.2}
.hero-card p{font-size:10px;line-height:1.7;color:var(--mute);margin-top:12px;width:250px}
.hero-card .btn{background:var(--blue);margin-top:18px;padding:8px 16px}

/* intro */
.intro{top:695px;left:0;width:1200px;text-align:center}
.intro h2{font-size:23px;line-height:1.2}
.intro p{width:600px;margin:20px auto 0;font-size:12px;line-height:1.5}
.badges{top:888px;left:297px;width:606px;height:106px;background:#f4f5f7;display:flex;align-items:center;gap:18px;padding:0 10px}
.badge-rect{width:114px;height:92px;border:2px solid #1d3b78;background:#e9eef7}
.badge-circ{width:62px;height:62px;border-radius:50%}
.sponsor{display:flex;flex-direction:column;align-items:center;gap:6px;font-size:9px;color:var(--blue);width:150px;text-align:center}
.sponsor span{width:140px;height:40px;background:var(--green)}

/* green band */
.band-bg{top:1045px;left:0;width:1200px;height:377px;background:var(--green)}
.band-notch{left:578px;top:1044px}
.band-title{top:1110px;left:0;width:1200px;text-align:center;color:#fff;font-size:24px;line-height:1.3}
.band-caption{left:369px;top:1395px;width:464px;text-align:center;font-weight:700;font-size:23px;color:#7fd3ee;line-height:1.4;text-shadow:0 0 2px #2a3a50,0 1px 3px rgba(0,0,0,.6)}

/* services */
.services-title{top:1525px;left:0;width:1200px;text-align:center;font-size:33px;line-height:1.35}
.service .label{display:flex;gap:12px;align-items:flex-start}
.service .label svg{flex:none;margin-top:4px}
.service small{display:block;font-size:10.5px;font-weight:500;color:var(--ink)}
.service h3{font-family:"Josefin Sans",sans-serif;font-weight:300;font-size:19px;color:var(--ink);margin-top:4px}
.service p{font-size:11px;line-height:1.6;margin-top:18px}
.service .btn{margin-top:14px;padding:6px 12px;font-size:10px}
.svc1{left:240px;top:1714px;width:310px}
.svc2{left:650px;top:2196px;width:295px}

/* attorneys */
.team-bg{top:2553px;left:0;width:1200px;height:400px;background:linear-gradient(90deg,#2d8fcb,#3aa4dc 50%,#2f95d0)}
.gray-bg{top:2953px;left:0;width:1200px;height:490px;background:var(--gray)}
.team-title{top:2628px;left:0;width:1200px;text-align:center;color:#fff;font-size:24px}
.card{top:2708px;width:226px;height:322px;background:#fff;text-align:center}
.card h4{font-size:12px;font-weight:500;color:var(--ink);margin-top:22px}
.card span{font-size:10.5px;color:var(--mute)}
.arrow{top:2810px}

/* quiz */
.quiz{left:607px;top:3107px;width:342px;height:271px;border:1px solid var(--ink);background:#fff;padding:48px 22px 0}
.quiz h3{font-family:"Josefin Sans",sans-serif;font-weight:300;font-size:21px;color:var(--ink)}
.quiz p{font-size:10.5px;line-height:1.6;margin-top:14px}
.quiz .btn{margin-top:18px;padding:9px 18px;font-size:10.5px}

/* video */
.video-title{left:269px;top:3468px;font-size:17px;line-height:1.3;color:var(--ink);font-family:"Josefin Sans",sans-serif;font-weight:300}
.video{left:267px;top:3529px;width:301px;height:175px;background:
  radial-gradient(ellipse 50px 60px at 150px 90px,rgba(196,156,130,.85),transparent 72%),
  radial-gradient(ellipse 110px 60px at 150px 175px,rgba(22,28,40,.95),transparent 75%),
  linear-gradient(180deg,#8c939c,#4c5562)}
.video .bar{position:absolute;top:0;left:0;width:100%;height:26px;background:rgba(0,0,0,.55);color:#fff;font-size:9px;padding:8px 10px 0 34px;white-space:nowrap;overflow:hidden}
.video .dot{position:absolute;left:8px;top:5px;width:16px;height:16px;border-radius:50%;background:#fff}
.video .play{position:absolute;left:130px;top:72px}
.divider{left:597px;top:3460px;width:1px;height:295px;background:var(--ink)}
.serve{left:624px;top:3478px;width:330px}
.serve .mini-brand{display:flex;align-items:center;gap:12px}
.serve .mini-brand i{width:50px;height:50px;border-radius:50%;background:var(--green)}
.serve .mini-brand b{font-size:10.5px;font-weight:600;letter-spacing:2px;color:var(--ink);text-transform:uppercase}
.serve h3{font-family:"Josefin Sans",sans-serif;font-weight:300;font-size:17px;color:var(--ink);margin-top:24px}
.serve p{font-size:10px;font-style:italic;line-height:1.7;margin-top:12px}
.serve .btn{margin-top:14px;padding:5px 12px;font-size:9.5px}

/* testimonials */
.reviews{top:3800px;left:0;width:1200px;height:550px;background:var(--green);overflow:hidden}
.ring{border-radius:50%;border:28px solid rgba(255,255,255,.16)}
.reviews-title{top:3900px;left:238px;color:#fff;font-size:24px;line-height:1.2}
.reviews-btn{left:784px;top:3924px;width:165px;height:34px;border:1px solid #fff;color:#fff;font-size:10.5px;text-align:center;line-height:32px}
.quote{top:3997px;width:345px;height:212px;background:#fff;padding:36px 28px}
.quote p{font-size:9px;font-style:italic;line-height:1.75;color:var(--mute)}
.quote-tip{top:4208px}
.quote-by{top:4236px;font-size:11.5px;color:#fff}

/* contact */
.ask{left:242px;top:4321px;width:306px;height:369px;background:var(--blue);padding:136px 0 0 44px;color:#fff}
.ask h3{font-family:"Josefin Sans",sans-serif;font-weight:300;font-size:23px;line-height:1.2}
.ask strong{display:block;font-family:"Josefin Sans",sans-serif;font-weight:300;font-size:26px;margin-top:14px}
.ask .outline{display:inline-block;border:1px solid #fff;font-size:10.5px;padding:9px 12px;margin-top:14px}
.form{left:548px;top:4321px;width:405px;height:369px;background:var(--dark);padding:88px 28px 0 28px;color:#fff}
.form h3{font-family:"Josefin Sans",sans-serif;font-weight:300;font-size:22px}
.form > p{font-size:10.5px;margin-top:8px}
.fields{display:flex;gap:14px;margin-top:24px}
.field{border:1px solid #aaa;height:30px;font-size:9.5px;padding:9px 14px;flex:1}
.field.area{height:78px;margin-top:14px}
.send{margin-top:18px;height:28px;background:var(--blue);text-align:center;font-size:12px;line-height:28px}

/* footer */
.footer{top:4772px;left:0;width:1200px;height:287px;background:var(--gray)}
.foot-col h5{font-size:12.5px;font-weight:500;color:var(--ink);margin-bottom:14px}
.foot-col li{list-style:none;font-size:9px;line-height:1.9}
.foot-col p{font-size:9px;line-height:1.8}
.sub-input{width:164px;height:30px;border:1px solid var(--ink);background:#fff}
.sub-btn{width:164px;height:28px;background:var(--dark);color:#fff;font-size:9.5px;text-align:center;line-height:28px;margin-top:6px}
.copy{left:239px;top:5027px;font-size:9.5px}
.social{left:860px;top:5021px;display:flex;gap:6px}
.social i{width:26px;height:26px;border-radius:50%;border:2px solid var(--blue)}
</style>
</head>
<body>

<header class="site-header abs">
  <div class="brand abs"><span class="brand-dot"></span><span class="brand-name">Meridale Family</span></div>
  <nav class="nav abs"><span>Home</span><span>About Us</span><span>Our Services</span><span>Testimonials</span><span>FAQ</span><span>Blog</span><span>Contact Us</span></nav>
  <div class="header-cta abs"><small>Schedule a Consultation Today</small><strong>(303) 555-0148</strong></div>
</header>

<div class="photo-hero abs" role="img" aria-label="Photo of smiling clients and advisors laughing together around a meeting table"></div>
<div class="hero-card abs">
  <h1 class="heading">Changing the<br>Way People Divorce.</h1>
  <p>Efficient and positive family legal transitions without costly, painful legal battles.</p>
  <span class="btn">Request A Free Consultation</span>
</div>

<section class="intro abs">
  <h2 class="heading">Efficient and positive family legal<br>transitions without costly, painful legal battles.</h2>
  <p>Many people don't want to add unnecessary financial and emotional costs to their divorce, but they need professional help to ensure they come away with a good parenting plan and fair financial outcomes. For these people, we offer Meridale Family™ divorce mediation or, when necessary, a Meridale Family™ lawyer.</p>
</section>
<div class="badges abs">
  <span class="badge-rect" role="img" aria-label="Listing badge"></span>
  <span class="badge-circ" style="background:#f39a2b" role="img" aria-label="Award badge"></span>
  <span class="badge-circ" style="width:70px;height:70px;background:#5a3d8c" role="img" aria-label="Recommendation badge"></span>
  <span class="badge-circ" style="width:70px;height:78px;background:#e0a924" role="img" aria-label="Award medal"></span>
  <div class="sponsor">We are proud to be corporate sponsors of<span role="img" aria-label="Sponsor badge"></span></div>
</div>

<div class="band-bg abs"></div>
<svg class="band-notch abs" width="44" height="22" viewBox="0 0 44 22"><polygon points="0,0 44,0 22,22" fill="#fff"/></svg>
<h2 class="band-title abs heading">Legal Malpractice &amp; Appellate Lawyers with<br>Over Half a Century of Award-Winning Experience.</h2>
<div class="photo-band abs" role="img" aria-label="Photo of a mother and children with backpacks looking out over mountains"></div>
<p class="band-caption abs">Divorce doesn't have to be<br>traumatic.</p>

<h2 class="services-title abs heading">Basic services we provide at<br>Meridale Family Law &amp; Mediation &nbsp;LLC are:</h2>

<article class="service svc1 abs">
  <div class="label">
    <svg width="40" height="34" viewBox="0 0 40 34" fill="none" stroke="#2f9dd8" stroke-width="1.6"><path d="M20 3v26M8 8h24M8 8l-5 11h10zM32 8l-5 11h10zM12 30h16"/></svg>
    <div><small>Divorce Mediation</small><h3>Meridale Family Mediation</h3></div>
  </div>
  <p>Mediation is possible when both spouses are willing to negotiate their divorce agreements in good faith, with the help of a neutral mediator. Meridale Family™ attorney-mediators are experienced family lawyers and are skilled at helping clients reach fair, workable agreements, without the cost and damage of the conventional divorce process.</p>
  <span class="btn">Read more</span>
</article>
<div class="photo-svc1 abs" role="img" aria-label="Photo of mediators reviewing documents at a laptop beside a justice statue"></div>

<div class="photo-svc2 abs" role="img" aria-label="Photo of a lawyer explaining options to a couple across a table"></div>
<article class="service svc2 abs">
  <div class="label">
    <svg width="40" height="40" viewBox="0 0 40 40" fill="none" stroke="#2f9dd8" stroke-width="1.6"><circle cx="13" cy="10" r="5"/><path d="M4 36V24a9 9 0 0 1 18 0v12M26 6v20M20 10h12M20 10l-3 7h6zM32 10l-3 7h6z"/></svg>
    <div><small>Divorce Lawyer</small><h3>Meridale Family Lawyer</h3></div>
  </div>
  <p>If mediation is not possible, you need a lawyer to advise, negotiate, and possibly advocate for you. Our experienced Meridale Family™ lawyers offer clear, confident, and highly effective advice and representation while attempting to minimize financial and emotional costs to you and your family.</p>
  <span class="btn">Read more</span>
</article>

<div class="team-bg abs"></div>
<div class="gray-bg abs"></div>
<h2 class="team-title abs heading">Attorneys and Mediators</h2>
<svg class="arrow abs" style="left:168px" width="18" height="40" viewBox="0 0 18 40"><path d="M16 2L2 20l14 18" fill="none" stroke="#fff" stroke-width="2"/></svg>
<svg class="arrow abs" style="left:1000px" width="18" height="40" viewBox="0 0 18 40"><path d="M2 2l14 18L2 38" fill="none" stroke="#fff" stroke-width="2"/></svg>
<div class="card abs" style="left:242px"><div class="portrait" role="img" aria-label="Portrait photo of attorney Daniel Voss"></div><h4>Daniel Voss</h4><span>Partner Attorney/Mediator</span></div>
<div class="card abs" style="left:485px"><div class="portrait" role="img" aria-label="Portrait photo of attorney Marcus Lindqvist"></div><h4>Marcus Lindqvist</h4><span>Partner Attorney/Mediator</span></div>
<div class="card abs" style="left:727px"><div class="portrait warm" role="img" aria-label="Portrait photo of attorney Claire Whitmore"></div><h4>Claire Whitmore</h4><span>Senior Attorney</span></div>

<div class="photo-quiz abs" role="img" aria-label="Photo of two children resting at a table while parents argue behind them"></div>
<div class="quiz abs">
  <h3>Mediation or Lawyer?</h3>
  <p>Our simple, free questionnaire can help you determine if you and your spouse are well suited for Meridale Family™ mediation, or if you may want legal representation for yourself.</p>
  <span class="btn">Take our free questionnaire</span>
</div>

<h3 class="video-title abs">Video : avoiding<br>harm to children in divorce</h3>
<div class="video abs" role="img" aria-label="Video still of an attorney speaking about protecting children in divorce">
  <div class="bar"><span class="dot"></span>Marcus Lindqvist - How to avoid harm to children…</div>
  <svg class="play" width="40" height="30" viewBox="0 0 40 30"><rect width="40" height="30" rx="6" fill="rgba(0,0,0,.65)"/><path d="M16 9l10 6-10 6z" fill="#fff"/></svg>
</div>
<div class="divider abs"></div>
<div class="serve abs">
  <div class="mini-brand"><i></i><b>Meridale Family</b></div>
  <h3>We are proud to serve your family</h3>
  <p>Meridale Family Law &amp; Mediation LLC currently serves the legal needs of Colorado residents (including same-sex and other alternative families) in Boulder County, Denver County, Broomfield County, Larimer County, Adams County, Weld County, and Jefferson County.</p>
  <span class="btn">Read more</span>
</div>

<section class="reviews abs">
  <div class="ring abs" style="left:680px;top:-40px;width:300px;height:300px"></div>
  <div class="ring abs" style="left:-170px;top:300px;width:360px;height:360px"></div>
</section>
<h2 class="reviews-title abs heading">Learn how our unique<br>mediation process has helped others</h2>
<div class="reviews-btn abs">View all testimonials</div>
<div class="quote abs" style="left:240px"><p>"I am so grateful for my experience with Meridale Family Law &amp; Mediation. I learned so much about myself and my capacity to love, grieve, and heal. You were so great at facilitating our difficult conversations, helping both of us feel validated, and coaching us on how to work well with each other moving forward in our new co-parenting relationship."</p></div>
<div class="quote abs" style="left:605px"><p>I really cannot thank you enough for all of your support and your excellent facilitation. I am almost certain that [my ex-husband] and I would not have been able to get through this so smoothly with anyone else. I love how you [grounded us at the] start [of] our sessions and it really helped me to step out of the fear and upset and focus on my boys and their well being. I will be forever grateful to you.</p></div>
<svg class="quote-tip abs" style="left:290px" width="24" height="14" viewBox="0 0 24 14"><polygon points="0,0 24,0 12,14" fill="#fff"/></svg>
<svg class="quote-tip abs" style="left:655px" width="24" height="14" viewBox="0 0 24 14"><polygon points="0,0 24,0 12,14" fill="#fff"/></svg>
<span class="quote-by abs" style="left:268px">Divorce mediation client</span>
<span class="quote-by abs" style="left:638px">Post-divorce mediation client</span>

<div class="ask abs">
  <h3>Get your<br>questions answered</h3>
  <strong>(303) 555-0148</strong>
  <span class="outline">Schedule a free information call</span>
</div>
<form class="form abs">
  <h3>Request Your Free Consultation</h3>
  <p>Send us a message or call us at (303) 555-0148</p>
  <div class="fields"><div class="field">Name*</div><div class="field">Email*</div></div>
  <div class="field area">Message*</div>
  <div class="send">Send message</div>
</form>

<footer class="footer abs">
  <div class="foot-col abs" style="left:239px;top:62px">
    <h5>Quick Links</h5>
    <ul><li>Home</li><li>Our Story</li><li>Attorneys &amp; Mediators</li><li>Client Service Staff</li><li>Testimonials</li><li>FAQ</li></ul>
  </div>
  <div class="foot-col abs" style="left:373px;top:92px">
    <ul><li>Blog</li><li>Contact Us</li><li>Resources</li><li>Meridale Family Mediation</li><li>Meridale Family Lawyer</li></ul>
  </div>
  <div class="foot-col abs" style="left:554px;top:62px">
    <h5>Address</h5>
    <p>Meridale Family Law &amp; Mediation LLC<br>1420 Aspenwood Lane, Suite 2 Boulder,<br>Colorado 80302</p>
    <p style="margin-top:8px">Phone: 1+ (303) 555-0148<br>Mail: info@meridalefamily.com</p>
  </div>
  <div class="foot-col abs" style="left:785px;top:62px">
    <h5 style="text-align:center">Subscribe with us</h5>
    <div class="sub-input"></div>
    <div class="sub-btn">Subscribe Now</div>
  </div>
</footer>
<p class="copy abs">© 2020 &nbsp;Meridale Family Law &amp; Mediation LLC. All Rights Reserved.</p>
<div class="social abs"><i></i><i></i><i style="border-color:#d9443a"></i></div>

</body>
</html>
```